Need exciting and bold trade show booth design

We focus on Roofing, Siding, Gutters.
We do both retail & insurance (Storm Damage) work. We offer financing.
We are an Halvern Tessit Preferred Contractor.
The following are just my thoughts:
Maybe have half of the backdrop to focus on insurance and half to focus on retail. Maybe have one side white with blue letters and one side white with blue letters? Maybe have the logo in the ,middle to separate the two sides? On the storm damage side have a storm and on the retail side have a calm sky? I am thank the stand alone display will have explained the warranty? Maybe have the highlight the four small sections won my website..... "Affordable Rates, Quick Response, Experienced Team, Veteran Owned."
5 Displays need graphics
10x10 display
Monitor display - logo with company name and logo only. Maybe a slogan added and/or graphic added.
Podium display - logo with company name or logo only. Maybe slogan added and/or graphic added.
Header Display - logo with name only
Stand alone display - Logo with company name and warranty workmanship information, "KSP". We offer a lifetime workmanship warranty, the "Keystone Shelter Pledge". I would like the stand alone banner to display the information about our "KSP" workmanship warranty.
Check out our website for more information.
www.blvtopcrew.com.
Potential roofing siding and gutter customers
Roofing
- Veteran Owned & Operated.

```html
<!DOCTYPE html>
<html lang="en">
<head>
<meta charset="utf-8">
<title>Bluvale Topcrew Contracting – Trade Show Booth</title>
<link rel="stylesheet" href="https://fonts.googleapis.com/css2?family=Montserrat:wght@700&family=Oswald:wght@400;500&family=Roboto+Condensed:wght@700&family=Open+Sans:wght@400;600&display=swap">
<style>
  :root {
    --brand-blue: #1a7cc5;
    --sky-blue: #1fc8e6;
    --deep-blue: #1769b3;
    --slate: #54575c;
    --slate-dark: #45484d;
    --white: #ffffff;
    --stage: #eceae8;
    --badge-red: #d2232a;
    --badge-pink: #e0679a;
  }
  * { margin: 0; padding: 0; box-sizing: border-box; }
  html, body { width: 1200px; height: 977px; overflow: hidden; background: var(--stage); }
  .canvas { position: relative; width: 1200px; height: 977px; }

  /* Header display */
  .header-display {
    position: absolute; left: 103px; top: 85px; width: 668px; height: 117px;
    border-radius: 28px;
    background: linear-gradient(90deg, var(--sky-blue) 0%, var(--brand-blue) 60%, var(--deep-blue) 100%);
  }
  .header-display .brand { position: absolute; left: 95px; top: 22px; }

  /* Brand lockup (invented name, single colour/weight) */
  .brand { display: flex; align-items: center; gap: 14px; }
  .brand-dot { border-radius: 50%; flex: none; }
  .brand-name {
    font-family: "Montserrat", sans-serif; font-weight: 700;
    line-height: 1.05; letter-spacing: 0.04em; text-transform: uppercase;
  }
  .header-display .brand-dot { width: 68px; height: 68px; background: var(--white); }
  .header-display .brand-name { font-size: 22px; color: var(--white); }

  /* Backdrop 10x10 */
  .backdrop {
    position: absolute; left: 30px; top: 225px; width: 815px; height: 633px;
    border-radius: 12px; overflow: hidden; background: var(--white);
  }
  .backdrop-art { position: absolute; inset: 0; }
  .backdrop .brand { position: absolute; left: 92px; top: 40px; }
  .backdrop .brand-dot { width: 96px; height: 96px; background: var(--brand-blue); }
  .backdrop .brand-name { font-size: 32px; color: var(--brand-blue); }

  .services {
    position: absolute; left: 545px; top: 54px; list-style: none;
    font-family: "Roboto Condensed", sans-serif; font-weight: 700;
    font-size: 28px; line-height: 30px; color: var(--white);
  }
  .services li { display: flex; align-items: center; gap: 12px; }
  .services li::before { content: ""; width: 11px; height: 11px; background: var(--white); }

  .panel-title {
    position: absolute; top: 180px; text-align: center; color: var(--white);
    font-family: "Oswald", sans-serif; font-weight: 500; font-size: 28px; line-height: 37px;
  }
  .panel-title.retail { left: 58px; width: 335px; }
  .panel-title.insurance { left: 416px; width: 334px; font-size: 27px; }

  .benefits { position: absolute; left: 0; top: 386px; width: 815px; height: 130px; }
  .benefit {
    position: absolute; top: 0; width: 140px; margin-left: -70px; text-align: center;
    font-family: "Open Sans", sans-serif; font-size: 18px; line-height: 22px; color: var(--white);
  }
  .benefit svg { display: block; margin: 0 auto 14px; height: 66px; }

  .partner-note {
    position: absolute; left: 58px; top: 580px; display: flex; align-items: center; gap: 8px;
    font-family: "Oswald", sans-serif; font-weight: 400; font-size: 17px; line-height: 18px; color: var(--slate-dark);
  }
  .partner-badge { width: 32px; height: 32px; background: var(--badge-red); }
  .system-badge {
    position: absolute; left: 690px; top: 584px; width: 74px; height: 30px;
    border-radius: 4px; background: var(--badge-pink);
  }
  .site-url {
    position: absolute; left: 285px; width: 245px; top: 597px; text-align: center;
    font-family: "Open Sans", sans-serif; font-weight: 600; font-size: 15px; color: var(--white);
  }

  /* Podium */
  .podium { position: absolute; left: 870px; top: 598px; width: 300px; height: 235px; }
  .podium-art { position: absolute; inset: 0; }
  .podium .brand { position: absolute; left: 52px; top: 36px; gap: 10px; }
  .podium .brand-dot { width: 46px; height: 46px; background: var(--brand-blue); }
  .podium .brand-name { font-size: 15px; color: var(--brand-blue); }
  .podium .site-url { left: 0; width: 300px; top: 162px; font-size: 12px; font-weight: 400; }
</style>
</head>
<body>
<main class="canvas">

  <section class="header-display" aria-label="Header display">
    <div class="brand">
      <span class="brand-dot"></span>
      <p class="brand-name">Bluvale<br>Topcrew<br>Contracting</p>
    </div>
  </section>

  <section class="backdrop" aria-label="10x10 backdrop">
    <svg class="backdrop-art" viewBox="0 0 815 633" width="815" height="633" aria-hidden="false">
      <defs>
        <linearGradient id="calmSky" x1="0" y1="0" x2="0" y2="1">
          <stop offset="0" stop-color="#1f7fcc"/>
          <stop offset="0.55" stop-color="#6fb0e2"/>
          <stop offset="1" stop-color="#d9e9f5"/>
        </linearGradient>
        <linearGradient id="stormSky" x1="0" y1="0" x2="0" y2="1">
          <stop offset="0" stop-color="#3f434a"/>
          <stop offset="0.5" stop-color="#7b7a78"/>
          <stop offset="1" stop-color="#a89f92"/>
        </linearGradient>
      </defs>
      <polygon points="467,45 750,45 750,148 520,148" fill="var(--slate)"/>
      <path d="M58 186 Q58 174 70 174 H381 Q393 174 393 186 V470 H58 Z" fill="url(#calmSky)" role="img" aria-label="Photo of a calm blue sky over the sea"/>
      <path d="M416 186 Q416 174 428 174 H738 Q750 174 750 186 V470 H416 Z" fill="url(#stormSky)" role="img" aria-label="Photo of storm-damaged houses under dark clouds"/>
      <path d="M0 570 C150 190 665 190 815 570 V633 H0 Z" fill="var(--white)"/>
      <path d="M0 590 C150 216 665 216 815 590 V633 H0 Z" fill="var(--brand-blue)"/>
      <path d="M0 578 C120 520 250 530 310 633 H0 Z" fill="var(--slate)"/>
      <path d="M0 592 C110 540 230 548 285 633 H0 Z" fill="var(--white)"/>
      <path d="M815 578 C695 520 565 530 505 633 H815 Z" fill="var(--slate)"/>
      <path d="M815 592 C705 540 585 548 530 633 H815 Z" fill="var(--white)"/>
      <path d="M285 633 C330 572 485 572 530 633 Z" fill="var(--slate)"/>
    </svg>

    <div class="brand">
      <span class="brand-dot"></span>
      <p class="brand-name">Bluvale<br>Topcrew<br>Contracting</p>
    </div>

    <ul class="services">
      <li>ROOFING</li>
      <li>SIDING</li>
      <li>GUTTERS</li>
    </ul>

    <h2 class="panel-title retail">Tessit Preferred<br>Contractor</h2>
    <h2 class="panel-title insurance">Insurance (Storm Damage)</h2>

    <div class="benefits">
      <div class="benefit" style="left:223px">
        <svg viewBox="0 0 56 66" width="56"><path d="M12 0 H44 V38 H56 L28 66 L0 38 H12 Z" fill="#fff"/><text x="28" y="37" text-anchor="middle" font-family="Montserrat, sans-serif" font-weight="700" font-size="28" fill="#1a7cc5">$</text></svg>
        Affordable<br>Rates
      </div>
      <div class="benefit" style="left:335px">
        <svg viewBox="0 0 68 66" width="68"><ellipse cx="34" cy="28" rx="33" ry="26" fill="#fff"/><path d="M16 46 L12 64 L30 52 Z" fill="#fff"/><path d="M22 26 L34 14 V21 C46 21 52 28 52 38 C47 31 42 30 34 30 V38 Z" fill="#1a7cc5"/></svg>
        Quick<br>Response
      </div>
      <div class="benefit" style="left:460px">
        <svg viewBox="0 0 80 66" width="80"><circle cx="18" cy="14" r="9" fill="#fff"/><circle cx="62" cy="14" r="9" fill="#fff"/><path d="M2 48 C2 32 8 26 18 26 C28 26 34 32 34 48 Z" fill="#fff"/><path d="M46 48 C46 32 52 26 62 26 C72 26 78 32 78 48 Z" fill="#fff"/><circle cx="40" cy="22" r="11" fill="#fff" stroke="#1a7cc5" stroke-width="2"/><path d="M20 66 C20 44 28 36 40 36 C52 36 60 44 60 66 Z" fill="#fff" stroke="#1a7cc5" stroke-width="2"/></svg>
        Experienced<br>Team
      </div>
      <div class="benefit" style="left:595px">
        <svg viewBox="0 0 80 66" width="80"><rect width="80" height="66" fill="#fff"/><g fill="#1a7cc5"><rect y="6" width="80" height="5"/><rect y="18" width="80" height="5"/><rect y="30" width="80" height="5"/><rect y="42" width="80" height="5"/><rect y="54" width="80" height="5"/><rect width="34" height="35"/></g></svg>
        Veteran<br>Owned
      </div>
    </div>

    <div class="partner-note">
      <span class="partner-badge"></span>
      <p>PREFERRED<br>CONTRACTOR</p>
    </div>
    <span class="system-badge"></span>
    <p class="site-url">www.blvtopcrew.com</p>
  </section>

  <section class="podium" aria-label="Podium display">
    <svg class="podium-art" viewBox="0 0 300 235" width="300" height="235">
      <rect x="0" y="14" width="300" height="196" fill="var(--white)"/>
      <path d="M12 205 C28 110 272 110 288 205 Z" fill="var(--brand-blue)"/>
      <rect x="4" y="198" width="292" height="37" rx="6" fill="var(--slate)"/>
      <rect x="0" y="0" width="300" height="16" rx="6" fill="#2a86cf"/>
    </svg>
    <div class="brand">
      <span class="brand-dot"></span>
      <p class="brand-name">Bluvale<br>Topcrew<br>Contracting</p>
    </div>
    <p class="site-url">www.blvtopcrew.com</p>
  </section>

</main>
</body>
</html>
```